Mendwise Partners
Project: Mendwise Partners
Mendwise Partners - Financial Services
Creative Brief
Professional
Karl Varner
Hillcrest Office Park 47 Bloem Street Kestrel Building Northbrook 2190
karl.varner@mendwisepartners-example.co.za
www.mendwisepartners-example.co.za
Try and use both the colour and black & white logos on the back.

```html
<!DOCTYPE html>
<html lang="en">
<head>
<meta charset="utf-8">
<title>Mendwise Partners – Business Cards</title>
<link href="https://fonts.googleapis.com/css2?family=Montserrat:wght@400;500;600&display=swap" rel="stylesheet">
<style>
  :root {
    --bg: #eceeef;
    --card: #ffffff;
    --brand-blue: #1d8ac4;
    --ink: #4a4d52;
    --muted: #7b7f85;
    --shadow: rgba(0, 0, 0, 0.12);
  }
  html, body {
    margin: 0;
    padding: 0;
    width: 1200px;
    height: 906px;
    overflow: hidden;
    background: var(--bg);
    font-family: "Montserrat", sans-serif;
  }
  .canvas {
    position: relative;
    width: 1200px;
    height: 906px;
  }
  .card {
    position: absolute;
    width: 520px;
    height: 289px;
    background: var(--card);
    box-shadow: 0 10px 30px var(--shadow);
    box-sizing: border-box;
  }
  .card--logo { left: 600px; top: 150px; }
  .card--details { left: 80px; top: 470px; }

  .wordmark {
    display: flex;
    align-items: center;
    gap: 10px;
    color: var(--brand-blue);
    font-weight: 600;
    letter-spacing: 0.5px;
    white-space: nowrap;
  }
  .wordmark__dot {
    width: 14px;
    height: 14px;
    border-radius: 50%;
    background: var(--brand-blue);
  }
  .card--logo .wordmark {
    position: absolute;
    left: 50%;
    top: 50%;
    transform: translate(-50%, -50%);
    font-size: 30px;
  }
  .card--details .wordmark {
    position: absolute;
    left: 50%;
    top: 40px;
    transform: translateX(-50%);
    font-size: 24px;
  }
  .person {
    position: absolute;
    left: 50%;
    top: 104px;
    transform: translateX(-50%);
    text-align: center;
  }
  .person__name {
    color: var(--brand-blue);
    font-size: 15px;
    font-weight: 500;
    letter-spacing: 1px;
    text-transform: uppercase;
  }
  .person__role {
    margin-top: 3px;
    color: var(--muted);
    font-size: 10px;
    letter-spacing: 1.5px;
    text-transform: uppercase;
  }
  .contact-list {
    position: absolute;
    list-style: none;
    margin: 0;
    padding: 0;
  }
  .contact-list--left { left: 28px; top: 26px; }
  .contact-list--right { left: 290px; top: 206px; }
  .contact-list li {
    display: flex;
    align-items: center;
    gap: 8px;
    height: 20px;
    font-size: 9px;
    color: var(--ink);
  }
  .contact-icon {
    width: 12px;
    height: 12px;
    flex: none;
  }
</style>
</head>
<body>
<div class="canvas">

  <section class="card card--logo" aria-label="Card back">
    <div class="wordmark"><span class="wordmark__dot"></span>Mendwise Partners</div>
  </section>

  <section class="card card--details" aria-label="Card front">
    <ul class="contact-list contact-list--left">
      <li>
        <svg class="contact-icon" viewBox="0 0 12 12"><rect width="12" height="12" rx="1.5" fill="var(--brand-blue)"/><path d="M6 2.5a2.3 2.3 0 0 0-2.3 2.3C3.7 6.6 6 9.5 6 9.5s2.3-2.9 2.3-4.7A2.3 2.3 0 0 0 6 2.5z" fill="#fff"/></svg>
        Hillcrest Office Park
      </li>
      <li>
        <svg class="contact-icon" viewBox="0 0 12 12"><rect width="12" height="12" rx="1.5" fill="var(--brand-blue)"/><path d="M3.5 2.8l1.3-.3.8 1.8-.9.6a5 5 0 0 0 2.4 2.4l.6-.9 1.8.8-.3 1.3C6 8.6 3.4 6 3.5 2.8z" fill="#fff"/></svg>
        011 555 0142
      </li>
      <li>
        <svg class="contact-icon" viewBox="0 0 12 12"><rect width="12" height="12" rx="1.5" fill="var(--brand-blue)"/><rect x="2.5" y="3.5" width="7" height="5" fill="none" stroke="#fff" stroke-width="0.9"/><path d="M2.5 3.5L6 6.3l3.5-2.8" fill="none" stroke="#fff" stroke-width="0.9"/></svg>
        karl.varner@mendwisepartners-example.co.za
      </li>
    </ul>

    <div class="wordmark"><span class="wordmark__dot"></span>Mendwise Partners</div>

    <div class="person">
      <div class="person__name">Dara Whitcombe</div>
      <div class="person__role">President</div>
    </div>

    <ul class="contact-list contact-list--right">
      <li>
        <svg class="contact-icon" viewBox="0 0 12 12"><rect width="12" height="12" rx="1.5" fill="var(--brand-blue)"/><rect x="2.5" y="3.5" width="7" height="5" fill="none" stroke="#fff" stroke-width="0.9"/><path d="M2.5 3.5L6 6.3l3.5-2.8" fill="none" stroke="#fff" stroke-width="0.9"/></svg>
        karl.varner@mendwisepartners-example.co.za
      </li>
      <li>
        <svg class="contact-icon" viewBox="0 0 12 12"><rect width="12" height="12" rx="1.5" fill="var(--brand-blue)"/><circle cx="6" cy="6" r="3.3" fill="none" stroke="#fff" stroke-width="0.9"/><path d="M2.7 6h6.6M6 2.7c-1.6 1.8-1.6 4.8 0 6.6M6 2.7c1.6 1.8 1.6 4.8 0 6.6" fill="none" stroke="#fff" stroke-width="0.7"/></svg>
        www.mendwisepartners-example.co.za
      </li>
      <li>
        <svg class="contact-icon" viewBox="0 0 12 12"><rect width="12" height="12" rx="1.5" fill="var(--brand-blue)"/><path d="M6 2.5a2.3 2.3 0 0 0-2.3 2.3C3.7 6.6 6 9.5 6 9.5s2.3-2.9 2.3-4.7A2.3 2.3 0 0 0 6 2.5z" fill="#fff"/></svg>
        Northbrook 2190
      </li>
    </ul>
  </section>

</div>
</body>
</html>
```